New residential property management company

I have a lot of name recognition in our smaller town due to owning a construction company here. I have now started a residential property management company representing landlords and tenants. Just trying to get my name out there and get some rentals to manage!

```html
<!DOCTYPE html>
<html lang="en">
<head>
<meta charset="utf-8">
<title>Harlow Property Management – Postcard</title>
<link href="https://fonts.googleapis.com/css2?family=Montserrat:wght@400;500;800&family=Barlow:ital,wght@0,300;0,500;0,600;0,700;1,400;1,500&family=Poppins:wght@700&family=Oswald:wght@600&display=swap" rel="stylesheet">
<style>
  :root{
    --stage:#3d3d3d;
    --label:#6b6b6b;
    --navy:#0b3470;
    --call-blue:#1556c9;
    --white:#ffffff;
    --panel:#e4e4e4;
    --ink:#1d1d1d;
    --ink-soft:#333333;
    --stamp:#a7a7a7;
    --rule:#9a9a9a;
  }
  *{margin:0;padding:0;box-sizing:border-box}
  html,body{width:1005px;height:1200px;overflow:hidden}
  body{background:var(--stage);position:relative;font-family:"Barlow",sans-serif}

  .side-label{
    position:absolute;left:57px;
    font-family:"Montserrat",sans-serif;font-weight:400;font-size:31px;
    color:var(--label);letter-spacing:1px;white-space:nowrap;
    transform:translate(-50%,-50%) rotate(-90deg);
  }
  .side-label--front{top:344px}
  .side-label--back{top:898px}

  .card{position:absolute;left:99px;width:802px;height:535px;overflow:hidden;background:var(--white)}
  .card--front{top:47px}
  .card--back{top:624px;height:534px;background:var(--panel)}
  .shape{position:absolute;inset:0}

  .hero-photo{
    clip-path:polygon(330px 0,802px 0,802px 535px,483px 535px);
    background:linear-gradient(180deg,#0a2c6c 0%,#2f5aa6 22%,#7d96bf 40%,#a59e91 58%,#8e8270 72%,#6b8a43 88%,#5f7d3a 100%);
  }
  .title-band{background:var(--navy);clip-path:polygon(0 120px,354px 120px,404px 295px,0 295px)}
  .intro-panel{background:var(--panel);clip-path:polygon(0 295px,404px 295px,443px 437px,0 437px)}

  .back-white{background:var(--white);clip-path:polygon(0 0,330px 0,483px 534px,0 534px)}
  .back-band{background:var(--navy);clip-path:polygon(0 0,318px 0,360px 150px,0 150px)}
  .agent-panel{background:var(--panel);clip-path:polygon(0 194px,374px 194px,441px 431px,0 431px)}

  .brand{position:absolute;display:flex;align-items:center;gap:20px;color:var(--ink);
    font-family:"Montserrat",sans-serif;font-weight:500}
  .brand__dot{width:54px;height:54px;border-radius:50%;background:var(--ink);flex:none}
  .brand__name{font-size:43px;line-height:1;letter-spacing:.5px;white-space:nowrap}
  .brand__tag{font-size:7.6px;letter-spacing:2.2px;margin-top:7px;text-align:right;white-space:nowrap}
  .card--front .brand{left:35px;top:34px}
  .card--back .brand{left:502px;top:430px}

  .service-title{position:absolute;left:25px;color:var(--white);font-family:"Montserrat",sans-serif;
    text-shadow:0 2px 3px rgba(0,0,0,.25);line-height:1}
  .service-title span{display:block}
  .service-title .light{font-weight:400}
  .service-title .bold{font-weight:800}
  .card--front .service-title{top:146px}
  .card--front .light{font-size:40px}
  .card--front .bold{font-size:47px;margin:2px 0 3px}
  .card--back .service-title{top:20px}
  .card--back .light{font-size:36px}
  .card--back .bold{font-size:42px;margin:2px 0}

  .tagline{position:absolute;left:360px;width:442px;top:28px;text-align:center;color:var(--white);
    font-family:"Montserrat",sans-serif;text-shadow:0 2px 4px rgba(0,0,0,.3)}
  .tagline__head{font-weight:800;font-size:44px;line-height:1.05;letter-spacing:.5px}
  .tagline__sub{font-weight:400;font-size:24px;line-height:1.12;margin-top:6px}

  .intro{position:absolute;left:25px;top:312px;width:380px;color:var(--ink-soft)}
  .intro__head{font-weight:600;font-size:21px;color:var(--ink);white-space:nowrap}
  .intro__body{font-weight:300;font-size:16.5px;line-height:21px;margin-top:13px}

  .contact{position:absolute;left:26px;color:var(--ink)}
  .card--front .contact{top:445px}
  .card--back .contact{top:444px}
  .contact__row{display:flex;align-items:center;gap:8px}
  .call-icon{width:41px;height:41px;flex:none}
  .call-icon circle{fill:var(--navy)}
  .card--back .call-icon circle{fill:var(--call-blue)}
  .contact__phone{font-family:"Poppins",sans-serif;font-weight:700;font-size:48px;line-height:1;letter-spacing:-.5px}
  .contact__line{font-weight:500;font-size:15.5px;margin-top:8px}

  .cta{position:absolute;left:27px;top:156px;font-family:"Oswald",sans-serif;font-weight:600;
    font-size:25px;line-height:1;color:var(--ink);letter-spacing:.3px}

  .agent-photo{position:absolute;left:26px;top:212px;width:126px;height:126px;border-radius:50%;
    background:#d2d2d2;border:3px solid var(--white);box-shadow:0 0 0 1px #cfcfcf}
  .agent-name{position:absolute;left:166px;top:215px;font-weight:700;font-size:21px;color:var(--ink);letter-spacing:.3px}
  .agent-role{position:absolute;left:166px;top:240px;font-weight:500;font-style:italic;font-size:15px;color:var(--ink)}
  .agent-bio{position:absolute;left:25px;top:267px;width:391px;font-style:italic;font-weight:400;
    font-size:12.6px;line-height:16.4px;color:var(--ink-soft);text-align:justify}
  .agent-bio::before{content:"";float:left;width:141px;height:82px}

  .stamp{position:absolute;left:665px;top:30px;width:104px;height:130px;background:var(--stamp)}
  .address-rule{position:absolute;left:503px;width:268px;height:1px;background:var(--rule)}
</style>
</head>
<body>

<div class="side-label side-label--front">FRONT PAGE</div>
<div class="side-label side-label--back">BACK PAGE</div>

<section class="card card--front">
  <div class="shape hero-photo" role="img" aria-label="Photo of a two-storey suburban house with a lawn under a blue sky, a smiling woman holding house keys in front"></div>
  <div class="shape title-band"></div>
  <div class="shape intro-panel"></div>

  <div class="brand">
    <span class="brand__dot"></span>
    <div>
      <div class="brand__name">HARLOW</div>
      <div class="brand__tag">PROPERTY MANAGEMENT LLC.</div>
    </div>
  </div>

  <h1 class="service-title">
    <span class="light">RESIDENTIAL</span>
    <span class="bold">PROPERTY</span>
    <span class="light">MANAGEMENT</span>
  </h1>

  <div class="tagline">
    <div class="tagline__head">WE ASSIST YOU</div>
    <div class="tagline__sub">KEEPING YOUR PROPERTIES<br>A HEALTHY BUSINESS</div>
  </div>

  <div class="intro">
    <h2 class="intro__head">Representing Landlords and Tenants</h2>
    <p class="intro__body">Our team of experts rely on more then 20 years of experience in Property Managment. Our assistance will help you to make the best out of your property.</p>
  </div>

  <div class="contact">
    <div class="contact__row">
      <svg class="call-icon" viewBox="0 0 40 40" aria-hidden="true"><circle cx="20" cy="20" r="20"/><path fill="#fff" transform="translate(8 8)" d="M6.62 10.79c1.44 2.830 3.76 5.14 6.59 6.59l2.2-2.2c.27-.27.67-.36 1.02-.24 1.12.37 2.33.57 3.57.57.55 0 1 .45 1 1V20c0 .55-.45 1-1 1-9.39 0-17-7.61-17-17 0-.55.45-1 1-1h3.5c.55 0 1 .45 1 1 0 1.25.2 2.45.57 3.57.11.35.03.74-.25 1.020l-2.2 2.2z"/></svg>
      <span class="contact__phone">(555)014-2290</span>
    </div>
    <p class="contact__line">48 Maple Lane | Lorem | W1 &nbsp;| &nbsp;info@harlowpm.com</p>
  </div>
</section>

<section class="card card--back">
  <div class="shape back-white"></div>
  <div class="shape back-band"></div>
  <div class="shape agent-panel"></div>

  <h2 class="service-title">
    <span class="light">RESIDENTIAL</span>
    <span class="bold">PROPERTY</span>
    <span class="light">MANAGEMENT</span>
  </h2>

  <p class="cta">CONTACT YOU MEDIATOR TODAY!</p>

  <div class="agent-photo" role="img" aria-label="Portrait photo of the agent"></div>
  <h3 class="agent-name">DEALER NAME</h3>
  <p class="agent-role">Designation</p>
  <p class="agent-bio">Lorem Ipsum is simply dummy text of the printing and typesetting industry. Lorem Ipsum has been the industry's standard dummy text.Lorem Ipsum is simply dummy text of the printing and typesetting industry. Lorem Ipsum has been the industry's standard dummy text. Lorem Ipsum is simply dummy text of the printing and typesetting industry. Lorem Ipsum has been the industry's standard dummy text. Lorem Ipsum is simply dummy text.</p>

  <div class="contact">
    <div class="contact__row">
      <svg class="call-icon" viewBox="0 0 40 40" aria-hidden="true"><circle cx="20" cy="20" r="20"/><path fill="#fff" transform="translate(8 8)" d="M6.62 10.79c1.44 2.83 3.76 5.14 6.59 6.59l2.2-2.2c.27-.27.67-.36 1.02-.24 1.12.37 2.33.57 3.57.57.55 0 1 .45 1 1V20c0 .55-.45 1-1 1-9.39 0-17-7.610-17-17 0-.55.45-1 1-1h3.5c.55 0 1 .45 1 1 0 1.25.2 2.45.57 3.57.11.35.03.74-.25 1.02l-2.2 2.2z"/></svg>
      <span class="contact__phone">(555)014-2290</span>
    </div>
    <p class="contact__line">48 Maple Lane | Lorem | W1 &nbsp;| &nbsp;info@harlowpm.com</p>
  </div>

  <div class="stamp"></div>
  <div class="address-rule" style="top:232px"></div>
  <div class="address-rule" style="top:283px"></div>
  <div class="address-rule" style="top:334px"></div>
  <div class="address-rule" style="top:384px"></div>

  <div class="brand">
    <span class="brand__dot"></span>
    <div>
      <div class="brand__name">HARLOW</div>
      <div class="brand__tag">PROPERTY MANAGEMENT LLC.</div>
    </div>
  </div>
</section>

</body>
</html>
```